Word template Letterhead for Australian Law Firm

We are a small law firm based in Manly, NSW, Australia. We have had a new logo designed for us and wish to freshen up the appearance of our letterhead. We require the letterhead to be in a word document that we can type over. This will not be a ‘printed’ letterhead because we send the majority of our correspondence via email. We would like to see a few options. We have attached our previous letterhead as well as the artwork for our new logo. We like the idea of a watermark across the bottom of the letter but the watermark must stay in place and we must be able to type over it. We are open to some colour throughout the letterhead because the majority of our correspondence is sent electronically. We also use electronic signatures. I have uploaded an example of this.The letterhead must include:-1. Our address details – including our phone number, physical address, website address etc. These details can be found on the copy of our previous letterhead;2. ABN Number;3. The words ‘Corvenda (NSW) Pty Ltd ACN 742 185 903 trading as Shipton & AssociatesLiability limited by a scheme approved under Professional Standards Legislation. The letterhead does not need to include the names and qualifications of the people working at the firm. Thank you.

Target Market(s)

Clients and other parties

Industry/Entity Type

Law Firm

Font styles to use
Other font styles liked:
• raleway, montserrat

Colors

Designer to choose colors to be used in the design.

Requirements
Must have
• Certain wording - please see project description.
• Must be a word document and must be able to type over the watermark etc.
Nice to have
• Watermark at the bottom of the letter.

```html
<!DOCTYPE html>
<html lang="en">
<head>
<meta charset="utf-8">
<title>Ferrow &amp; Associates Letterhead</title>
<link rel="stylesheet" href="https://fonts.googleapis.com/css2?family=Open+Sans:wght@600;700&family=Source+Sans+3:wght@400;700&family=Raleway:wght@600&display=swap">
<style>
  :root {
    --paper: #ffffff;
    --ink: #3c3c3c;
    --ink-strong: #1f1f1f;
    --brand-blue: #3d4aa3;
    --brand-gold: #c2aa72;
    --rule: #6b6b6b;
    --sig-tone: #ececec;
  }
  html, body {
    margin: 0;
    padding: 0;
    width: 980px;
    height: 1200px;
    overflow: hidden;
    background: var(--paper);
  }
  .letterhead {
    position: relative;
    width: 980px;
    height: 1200px;
    background: var(--paper);
    color: var(--ink);
  }
  .brand {
    position: absolute;
    left: 83px;
    top: 150px;
    display: flex;
    align-items: center;
    gap: 12px;
  }
  .brand-dot {
    width: 18px;
    height: 18px;
    border-radius: 50%;
    background: var(--brand-blue);
  }
  .brand-name {
    font-family: "Raleway", sans-serif;
    font-weight: 600;
    font-size: 22px;
    letter-spacing: 0.8px;
    color: var(--brand-blue);
  }
  .contact {
    position: absolute;
    right: 97px;
    top: 101px;
    text-align: right;
    font-family: "Open Sans", sans-serif;
    font-weight: 700;
    font-size: 12px;
    line-height: 15px;
    color: var(--ink-strong);
  }
  .contact p { margin: 0; }
  .letter {
    position: absolute;
    left: 83px;
    top: 276px;
    width: 807px;
    font-family: "Source Sans 3", sans-serif;
  }
  .letter-title {
    margin: 0 0 20px 0;
    font-size: 21px;
    font-weight: 700;
    color: var(--ink-strong);
  }
  .letter-body p {
    margin: 0 0 19.7px 2px;
    font-size: 15.4px;
    line-height: 19.7px;
    text-align: justify;
    hyphens: auto;
    color: var(--ink);
  }
  .signature {
    position: absolute;
    left: 706px;
    top: 940px;
    width: 177px;
    height: 60px;
    background: linear-gradient(90deg, #fafafa, var(--sig-tone));
  }
  .footer-rule {
    position: absolute;
    left: 93px;
    top: 1056px;
    width: 798px;
    height: 1px;
    background: var(--rule);
  }
  .accreditation {
    position: absolute;
    left: 145px;
    top: 1078px;
    width: 64px;
    height: 64px;
    border-radius: 50%;
    background: var(--ink-strong);
  }
  .legal {
    position: absolute;
    left: 230px;
    top: 1094px;
    margin: 0;
    font-family: "Open Sans", sans-serif;
    font-weight: 600;
    font-size: 13.4px;
    line-height: 16.5px;
    color: var(--ink-strong);
  }
</style>
</head>
<body>
<main class="letterhead">
  <header>
    <div class="brand">
      <span class="brand-dot"></span>
      <span class="brand-name">Ferrow &amp; Associates</span>
    </div>
    <address class="contact">
      <p>SUITE 4, 12 BELGRAVE LANE</p>
      <p>MANLY NSW 2095</p>
      <p>TELEPHONE: (02) 9481 3720</p>
      <p>FACSIMILE: (02) 9481 3721</p>
      <p>Email: reception@corvendalaw.com.au</p>
      <p>www.ferrowassociates.com.au</p>
      <p>ABN: 63 742 185 903</p>
    </address>
  </header>

  <article class="letter">
    <h1 class="letter-title">Lorem ipsum dolor sit amet</h1>
    <div class="letter-body">
      <p>Lorem ipsum dolor sit amet, consectetur adipiscing elit, sed do eiusmod tempor incididunt ut labore et dolore magna aliqua. Ut enim ad minim veniam, quis nostrud exercitation ullamco laboris nisi ut aliquip ex ea commodo consequat. Duis aute irure dolor in reprehenderit in voluptate velit esse cillum dolore eu fugiat nulla pariatur. Excepteur sint occaecat cupidatat non proident, sunt in culpa qui officia deserunt mollit anim id est laborum Sed ut perspiciatis unde omnis iste natus error sit voluptatem accusantium doloremque laudantium, totam rem aperiam, eaque ipsa quae ab illo inventore veritatis et quasi architecto beatae vitae dicta sunt explicabo. Nemo enim ipsam voluptatem quia voluptas sit aspernatur aut odit aut fugit, sed quia consequuntur magni dolores eos qui ratione voluptatem sequi nesciunt. Neque porro quisquam est, qui dolorem ipsum quia dolor sit amet, consectetur, adipisci velit, sed quia non numquam eius modi tempora incidunt ut labore et dolore magnam aliquam quaerat voluptatem. Ut enim ad minima veniam, quis nostrum exercitationem ullam corporis suscipit laboriosam, nisi ut aliquid ex ea commodi consequatur? Quis autem vel eum iure reprehenderit qui in ea voluptate velit esse quam nihil molestiae consequatur, vel illum qui dolorem eum fugiat quo voluptas nulla pariatur?</p>
      <p>Lorem ipsum dolor sit amet, consectetur adipiscing elit, sed do eiusmod tempor incididunt ut labore et dolore magna aliqua. Ut enim ad minim veniam, quis nostrud exercitation ullamco laboris nisi ut aliquip ex ea commodo consequat. Duis aute irure dolor in reprehenderit in voluptate velit esse cillum dolore eu fugiat nulla pariatur. Excepteur sint occaecat cupidatat non proident, sunt in culpa qui officia deserunt mollit anim id est laborum Sed ut perspiciatis unde omnis iste natus error sit voluptatem accusantium doloremque laudantium, totam rem aperiam, eaque ipsa quae ab illo inventore veritatis et quasi architecto beatae vitae dicta sunt explicabo. Nemo enim ipsam voluptatem quia voluptas sit aspernatur aut odit aut fugit, sed quia consequuntur magni dolores eos qui ratione voluptatem sequi nesciunt. Neque porro quisquam est, qui dolorem ipsum quia dolor sit amet, consectetur, adipisci velit, sed quia non numquam eius modi tempora incidunt ut labore et dolore magnam aliquam quaerat voluptatem. Ut enim ad minima veniam, quis nostrum exercitationem ullam corporis suscipit laboriosam, nisi ut aliquid ex ea commodi consequatur? Quis autem vel eum iure reprehenderit qui in ea voluptate velit esse quam nihil molestiae consequatur, vel illum qui dolorem eum fugiat quo voluptas nulla pariatur?</p>
      <p>Lorem ipsum dolor sit amet, consectetur adipiscing elit, sed do eiusmod tempor incididunt ut labore et dolore magna aliqua. Ut enim ad minim veniam, quis nostrud exercitation ullamco laboris nisi ut aliquip ex ea commodo consequat. Duis aute irure dolor in reprehenderit in voluptate velit esse cillum dolore eu fugiat nulla pariatur.</p>
    </div>
  </article>

  <div class="signature" role="img" aria-label="Handwritten electronic signature"></div>

  <footer>
    <div class="footer-rule"></div>
    <div class="accreditation" role="img" aria-label="Accredited specialist badge"></div>
    <p class="legal">Corvenda (NSW) Pty Ltd ACN 742 185 903 trading as Ferrow &amp; AssociatesLiability limited<br>by a scheme approved under Professional Standards Legislation</p>
  </footer>
</main>
</body>
</html>
```